Have Logo - Need Business Card Design!!!

I am looking for a business card design for a real estate development business. The company name is MV Realty Partners. I already have a logo created by Sketch Harbor and would like this logo to be incorporated into the design. I have uploaded the files. The card needs to be professional, but visually interesting. Not necessary to be double-sided, but if you want to get creative and can think of something to put on the back then have at it.

Target Market(s)

The target audience for these business cards will be professionals in the real estate industry.

Industry/Entity Type

Real Estate

Requirements
Must have
• The business card must have all the necessary items for a business card, i.e. company name, our logo, name (however, not title necessary), office address, office phone number, cell number, fax number, website address, etc.

You can use the information below for the card:

Gregory L. Hanlon
782 Marlowe Avenue
San Francisco, California 94127

www.mvrealtypartners.example
ghanlon@mvrealtypartners.example
Office: 415-555-0142
Fax: 415-555-0143
Cell: 415-555-0186

```html
<!DOCTYPE html>
<html lang="en">
<head>
<meta charset="utf-8">
<title>Calder Ridge Estates — Business Card</title>
<link rel="stylesheet" href="https://fonts.googleapis.com/css2?family=Montserrat:wght@400;500;600&display=swap">
<style>
  :root {
    --green: #0e8a44;
    --navy: #1f3a7a;
    --white: #ffffff;
    --paper: #f6f6f6;
    --mist: #e3e3ee;
    --stage: #d9d6d0;
  }
  * { box-sizing: border-box; margin: 0; padding: 0; }
  html, body { width: 1200px; height: 1023px; overflow: hidden; }
  body {
    background: var(--stage);
    font-family: "Montserrat", Arial, sans-serif;
    display: flex;
    flex-direction: column;
    align-items: center;
    justify-content: center;
    gap: 75px;
  }
  .card {
    position: relative;
    width: 700px;
    height: 400px;
    overflow: hidden;
    box-shadow: 0 6px 18px rgba(0,0,0,0.18);
  }

  /* Front */
  .card--front { background: linear-gradient(135deg, var(--white), var(--paper)); }
  .brand {
    position: absolute;
    left: 0;
    right: 64px;
    top: 50%;
    transform: translateY(-50%);
    text-align: center;
  }
  .brand__name {
    color: var(--green);
    font-weight: 600;
    font-size: 38px;
    letter-spacing: 0.04em;
  }
  .web-band {
    position: absolute;
    right: 0; top: 0;
    width: 64px; height: 100%;
    background: var(--navy);
    display: flex;
    align-items: center;
    justify-content: center;
  }
  .web-band__url {
    color: var(--white);
    font-size: 13px;
    font-weight: 500;
    letter-spacing: 0.2em;
    text-transform: uppercase;
    white-space: nowrap;
    transform: rotate(-90deg);
  }

  /* Back */
  .card--back { background: var(--mist); }
  .edge-strip {
    position: absolute;
    left: 0; top: 0;
    width: 28px; height: 100%;
    background: var(--navy);
  }
  .contact-panel {
    position: absolute;
    left: 28px; top: 0;
    width: 400px; height: 100%;
    background: var(--green);
    color: var(--white);
    padding: 58px 40px;
    display: flex;
    flex-direction: column;
    justify-content: center;
  }
  .contact__name {
    font-size: 20px;
    font-weight: 600;
    letter-spacing: 0.12em;
    text-transform: uppercase;
    margin-bottom: 18px;
  }
  .contact__line {
    font-size: 13px;
    letter-spacing: 0.1em;
    text-transform: uppercase;
    line-height: 1.75;
  }
  .contact__line--lower { text-transform: none; letter-spacing: 0.06em; }
  .contact__gap { height: 14px; }
</style>
</head>
<body>
  <section class="card card--front" aria-label="Card front">
    <div class="brand">
      <span class="brand__name">Calder Ridge Estates</span>
    </div>
    <div class="web-band">
      <span class="web-band__url">www.calderridge.example</span>
    </div>
  </section>

  <section class="card card--back" aria-label="Card back">
    <div class="edge-strip"></div>
    <div class="contact-panel">
      <p class="contact__name">Gregory L. Hanlon</p>
      <p class="contact__line">782 Marlowe Avenue</p>
      <p class="contact__line">San Francisco, California 94127</p>
      <div class="contact__gap"></div>
      <p class="contact__line">Office: 415-555-0142</p>
      <p class="contact__line">Fax: 415-555-0143</p>
      <p class="contact__line">Cell: 415-555-0186</p>
      <div class="contact__gap"></div>
      <p class="contact__line contact__line--lower">www.calderridge.example</p>
      <p class="contact__line contact__line--lower">ghanlon@calderridge.example</p>
    </div>
  </section>
</body>
</html>
```